New Company Introduction

We have launched a new business channel and need an online 'brochure' that we can use to announce us. Short, no more than 5 pages, clean, simple and changeable as we develop. See our new website for direction www.skyvellcare-example.com the introduction is to be issued to insurance companies, government departments and private clinics

Industry/Entity Type

Government

Font styles to use
Sans Serif

```html
<!DOCTYPE html>
<html lang="en">
<head>
<meta charset="utf-8">
<title>Skyvell Care – Back Page</title>
<link href="https://fonts.googleapis.com/css2?family=Source+Sans+3:wght@300;400;600;700&display=swap" rel="stylesheet">
<style>
  :root {
    --page-bg: #eceef1;
    --white: #ffffff;
    --band-blue: #3f8ac9;
    --stripe-lavender: #a4b4dd;
    --pill-teal: #76ab9e;
    --ink: #111418;
    --text-grey: #3a3d42;
    --link-blue: #3d86c6;
    --brand-grey: #6f8396;
    --photo-light: #f4f6f8;
    --photo-mid: #dbe3ea;
    --photo-coat: #f7f8f9;
  }
  * { margin: 0; padding: 0; box-sizing: border-box; }
  html, body {
    width: 1200px; height: 971px; overflow: hidden;
    background: var(--page-bg);
    font-family: "Source Sans 3", "Helvetica Neue", Arial, sans-serif;
  }
  .back-page {
    position: absolute; left: 20px; top: 72px;
    width: 1160px; height: 827px;
    background: var(--white);
    box-shadow: 0 2px 10px rgba(0,0,0,0.12);
  }
  .hero-photo {
    height: 439px;
    background:
      linear-gradient(90deg, transparent 78%, var(--photo-coat) 86%),
      linear-gradient(160deg, var(--photo-light) 0%, var(--photo-mid) 55%, var(--photo-light) 100%);
  }
  .contact-band {
    height: 182px; background: var(--band-blue);
    position: relative; text-align: center;
  }
  .headline {
    position: absolute; left: 0; right: 0; top: 12px;
    font-weight: 600; font-size: 33px; color: var(--ink);
    letter-spacing: -0.2px;
  }
  .availability-pill {
    position: absolute; left: 61px; top: 67px;
    width: 1005px; height: 31px; border-radius: 6px;
    background: var(--pill-teal); color: var(--white);
    font-size: 17px; line-height: 31px; letter-spacing: 1.8px;
    word-spacing: 4px;
  }
  .call-line {
    position: absolute; left: 0; right: 0; top: 120px;
    color: var(--white); font-weight: 600; font-size: 34px;
  }
  .call-line .number { font-size: 42px; margin-left: 10px; }
  .accent-stripe { height: 15px; background: var(--stripe-lavender); }
  .footer { position: relative; height: 191px; }
  .address {
    position: absolute; left: 62px; top: 26px;
    font-size: 16px; line-height: 22px; color: var(--text-grey);
  }
  .email {
    position: absolute; left: 62px; top: 82px;
    font-size: 18px; color: var(--ink);
  }
  .website {
    position: absolute; left: 62px; top: 127px;
    font-size: 25px; font-weight: 600; color: var(--link-blue);
  }
  .brand {
    position: absolute; left: 640px; top: 102px;
    display: flex; align-items: center; gap: 18px;
  }
  .brand-dot { width: 40px; height: 40px; border-radius: 50%; background: var(--link-blue); }
  .brand-name { font-size: 34px; font-weight: 300; color: var(--brand-grey); }
</style>
</head>
<body>
  <main class="back-page">
    <div class="hero-photo" role="img" aria-label="Photo of a doctor in a white coat holding a stethoscope over a pale blue background with a heartbeat line"></div>
    <section class="contact-band">
      <h1 class="headline">We are always happy to talk people through the process and options</h1>
      <p class="availability-pill">Our specialists are available 24hrs. Please contact us on our UK and International telephone number</p>
      <p class="call-line">Call Us: <span class="number">+44 (0)203 555 0147</span></p>
    </section>
    <div class="accent-stripe"></div>
    <footer class="footer">
      <p class="address">SKVC, Skyvell Care Ltd,<br>Ashford Vale, Westmere, United Kingdom, AV12 3XY</p>
      <p class="email">Email: operations@skyvellcare-example.com</p>
      <p class="website">www.skyvellcare-example.com</p>
      <div class="brand">
        <span class="brand-dot"></span>
        <span class="brand-name">Skyvell Care</span>
      </div>
    </footer>
  </main>
</body>
</html>
```